Use your magic to make a startup company look established*

We are in need of a website that gives the appearance that we are established rather than new. Our audience is comprised of senior executives in technology professional services companies, financial people (conservative) that invest in them, and executives in companies that are in need of their services. The site therefore needs to lean towards the conservative side while being modern and professional.

This should be a fairly simple site.

- About us
- Services
- Contacts
- Content (Articles)

It should be SEO friendly and easy to add content or sub pages. A responsive design is mandatory.

Target Market(s)

We work with executives and investors in professional services companies to more effectively compete in the already crowded “digital transformation” market.

Industry/Entity Type

Professional Service

Coding

Coded - Design and coding required

Number of Pages Required

5+ page

Font styles to use
Sans Serif

Requirements
Must have
• - Responsive design
- Easy to add/change content
- Easy to add additional pages

```html
<!DOCTYPE html>
<html lang="en">
<head>
<meta charset="utf-8">
<title>Keystone Ridge Advisors</title>
<link href="https://fonts.googleapis.com/css2?family=Montserrat:wght@400;500;600;700&display=swap" rel="stylesheet">
<style>
:root{
  --gold:#e3b93f;
  --gold-deep:#a8802a;
  --grey:#7d7d7d;
  --ink:#232323;
  --dark:#1d1d1d;
  --cream:#f9f6ee;
  --text:#3a3a3a;
  --muted:#8a8a8a;
  --line:#dcdcdc;
}
*{box-sizing:border-box;margin:0;padding:0}
html,body{width:1200px;height:2933px;overflow:hidden}
body{position:relative;font-family:'Montserrat',sans-serif;color:var(--text);background:#fff}
.abs{position:absolute}
.btn{position:absolute;background:linear-gradient(90deg,#d9ac31,#ecc956);color:#fff;font-weight:600;font-size:14px;letter-spacing:.5px;display:flex;align-items:center;justify-content:center}
.btn::after{content:"";position:absolute;right:-8px;top:-6px;width:22px;height:calc(100% + 12px);border:2px solid var(--gold-deep);border-left:none}
.bracket-frame{position:absolute}
.bracket-frame .t-gold{position:absolute;left:0;top:0;height:12px;background:linear-gradient(90deg,#e7c04b,#d4aa3a)}
.bracket-frame .l-gold{position:absolute;left:0;top:0;width:7px;background:linear-gradient(180deg,#e7c04b,#c79a2d)}
.bracket-frame .t-grey{position:absolute;right:0;top:0;height:12px;background:linear-gradient(90deg,#555,#9a9a9a)}
.bracket-frame .r-grey{position:absolute;right:0;top:0;width:7px;background:linear-gradient(180deg,#777,#aaa)}
.bracket-frame .r-gold{position:absolute;right:0;bottom:0;width:7px;background:linear-gradient(180deg,#d6ad3e,#a97f26)}
.bracket-frame .b-gold{position:absolute;right:0;bottom:0;height:9px;background:linear-gradient(90deg,#b88d2d,#9b7222)}
.section-title{position:absolute;left:0;width:1200px;text-align:center;font-size:44px;font-weight:600;letter-spacing:2px;color:#9a9a9a}
/* header */
.brand{position:absolute;left:143px;top:14px;display:flex;align-items:center;gap:12px}
.brand .mark{width:12px;height:12px;border:2px solid var(--gold)}
.brand span{font-size:16px;font-weight:500;letter-spacing:1.5px;color:var(--grey);line-height:19px}
.nav{position:absolute;top:40px;left:507px;display:flex;gap:40px;font-size:14px;font-weight:500;color:#555;letter-spacing:.5px}
/* hero */
.hero-bg{left:0;top:99px;width:1200px;height:609px;background:#3b3422}
.hero-panel{left:46px;top:154px;width:1154px;height:554px;background:radial-gradient(ellipse at 85% 40%,#4a4a4a 0%,#262626 45%,#1f1f1f 100%)}
.hero-topband{left:46px;top:99px;width:943px;height:55px;background:#3a3322}
.hero-bar{left:144px;top:237px;width:5px;height:253px;background:var(--gold)}
.hero-title{left:183px;top:236px;color:#fff;font-size:76px;font-weight:600;letter-spacing:2px;line-height:85px}
.dots{left:1129px;top:380px;display:flex;flex-direction:column;gap:15px}
.dots i{width:8px;height:8px;border-radius:50%;background:#fff;display:block}
.dots i.on{background:var(--gold)}
/* about */
.about-photo{left:170px;top:814px;width:307px;height:312px;background:radial-gradient(circle at 45% 45%,#7a7a7a,#2b2b2b 70%,#1a1a1a)}
.about-title{left:591px;top:793px;font-size:44px;font-weight:600;letter-spacing:2px;color:#9a9a9a}
.about-text{left:591px;top:872px;width:470px;font-size:14px;line-height:26.5px;color:#333}
/* services */
.services-bg{left:0;top:1289px;width:1200px;height:470px;background:var(--cream)}
.services-ext{left:442px;top:1759px;width:758px;height:85px;background:var(--cream)}
.card{position:absolute;top:1470px;width:218px;height:217px}
.card .body{position:absolute;left:0;top:0;width:100%;height:100%;text-align:center;padding-top:24px}
.card .icon{width:58px;height:58px;margin:0 auto;border:2px solid #333;border-radius:50%}
.card h3{margin-top:24px;font-size:16px;font-weight:500;letter-spacing:.5px;color:#222}
.card p{margin:12px auto 0;width:170px;font-size:11.5px;line-height:19px;color:var(--muted)}
.arrow{position:absolute;top:1556px;width:45px;height:45px;border:1px solid #777;border-radius:50%;display:flex;align-items:center;justify-content:center}
/* contact */
.field{position:absolute;border:1px solid var(--line);background:#fff;font-size:16px;color:#555;padding:17px 22px}
/* footer */
.foot-gold{left:0;top:2448px;width:758px;height:485px;background:linear-gradient(180deg,#e4be45,#c49a33)}
.foot-dark{left:23px;top:2471px;width:1177px;height:462px;background:var(--ink)}
.foot-dark-right{left:758px;top:2534px;width:442px;height:399px;background:var(--ink)}
.foot-name{left:165px;top:2590px;font-size:23px;font-weight:500;letter-spacing:3px;line-height:29px;color:#a9a9a9;display:flex;gap:18px;align-items:flex-start}
.foot-name .mark{width:16px;height:16px;border:2px solid var(--gold);margin-top:6px}
.social{position:absolute;top:2608px;width:62px;height:62px;border:1.5px solid #fff;border-radius:50%}
.ql-title{left:910px;top:2603px;font-size:19px;font-weight:700;color:var(--gold);letter-spacing:.5px}
.ql{left:910px;top:2648px;display:flex;flex-direction:column;gap:19px;font-size:15px;color:#fff}
.news-title{left:163px;top:2757px;font-size:19px;font-weight:700;color:var(--gold);letter-spacing:.5px}
.news-input{left:421px;top:2747px;width:419px;height:42px;background:#fff;border:2px solid var(--gold);font-size:11px;color:#555;padding:13px 23px}
.news-btn{left:738px;top:2749px;width:100px;height:38px;background:var(--gold);color:#fff;font-weight:700;font-size:16px;display:flex;align-items:center;justify-content:center}
.copy{left:0;top:2860px;width:1200px;text-align:center;font-size:15px;color:#fff}
</style>
</head>
<body>
<header>
  <div class="brand"><div class="mark"></div><span>KEYSTONE<br>RIDGE<br>ADVISORS</span></div>
  <nav class="nav"><span>HOME</span><span>ABOUT US</span><span>SERVICES</span><span>CONTACT US</span></nav>
  <div class="btn" style="left:962px;top:34px;width:90px;height:30px">LOGIN</div>
</header>

<section class="hero">
  <div class="abs hero-bg"></div>
  <div class="abs hero-topband"></div>
  <div class="abs hero-panel" role="img" aria-label="Dark abstract background of floating geometric network shapes"></div>
  <div class="abs hero-bar"></div>
  <h1 class="abs hero-title">KEYSTONE<br>RIDGE<br>ADVISORS</h1>
  <div class="btn" style="left:185px;top:528px;width:146px;height:38px">GET STARTED</div>
  <div class="abs dots"><i></i><i></i><i class="on"></i><i></i><i></i></div>
</section>

<section class="about">
  <div class="bracket-frame" style="left:143px;top:789px;width:360px;height:359px">
    <div class="t-gold" style="width:243px"></div>
    <div class="l-gold" style="height:256px"></div>
    <div class="t-grey" style="width:106px"></div>
    <div class="r-grey" style="height:106px"></div>
    <div class="r-gold" style="height:240px"></div>
    <div class="b-gold" style="width:123px"></div>
  </div>
  <div class="abs about-photo" role="img" aria-label="Monochrome photo of a smartphone with a rising stock chart"></div>
  <h2 class="abs about-title">ABOUT US</h2>
  <p class="abs about-text">Keystone Ridge Advisors is a professional firm that advises professional services companies on how to increase revenue and margins, and systematically acquire new clients.Our clients can expect to become strategic partners with their clients rather than just vendors. We work with executives at professional services firms and institutional investors seeking to increase the value of their investments in services firms.</p>
  <div class="btn" style="left:594px;top:1090px;width:146px;height:38px">READ MORE</div>
</section>

<section class="services">
  <div class="abs services-bg"></div>
  <div class="abs services-ext"></div>
  <h2 class="section-title" style="top:1360px">OUR SERVICES</h2>
  <div class="arrow" style="left:71px"><svg width="14" height="20"><path d="M10 2 2 10l8 8" fill="none" stroke="#555" stroke-width="2"/></svg></div>
  <div class="arrow" style="left:1085px"><svg width="14" height="20"><path d="M4 2l8 8-8 8" fill="none" stroke="#555" stroke-width="2"/></svg></div>

  <div class="card" style="left:143px">
    <div class="bracket-frame" style="left:0;top:0;width:218px;height:217px"><div class="t-gold" style="width:150px;height:6px"></div><div class="l-gold" style="height:162px;width:6px"></div><div class="t-grey" style="width:60px;height:6px"></div><div class="r-grey" style="height:65px;width:6px"></div><div class="r-gold" style="height:145px;width:6px"></div><div class="b-gold" style="width:75px;height:7px"></div></div>
    <div class="body"><div class="icon"></div><h3>EXPERIENCED</h3><p>Lorem ipsum dolor sit amonsectetur adipiscing incididunt ut labore et</p></div>
  </div>
  <div class="card" style="left:375px">
    <div class="bracket-frame" style="left:0;top:0;width:218px;height:217px"><div class="t-gold" style="width:150px;height:6px"></div><div class="l-gold" style="height:162px;width:6px"></div><div class="t-grey" style="width:60px;height:6px"></div><div class="r-grey" style="height:65px;width:6px"></div><div class="r-gold" style="height:145px;width:6px"></div><div class="b-gold" style="width:75px;height:7px"></div></div>
    <div class="body"><div class="icon"></div><h3>KNOWLEDGEABLE</h3><p>Lorem ipsum dolor sit amonsectetur adipiscing incididunt ut labore et</p></div>
  </div>
  <div class="card" style="left:606px">
    <div class="bracket-frame" style="left:0;top:0;width:218px;height:217px"><div class="t-gold" style="width:150px;height:6px"></div><div class="l-gold" style="height:162px;width:6px"></div><div class="t-grey" style="width:60px;height:6px"></div><div class="r-grey" style="height:65px;width:6px"></div><div class="r-gold" style="height:145px;width:6px"></div><div class="b-gold" style="width:75px;height:7px"></div></div>
    <div class="body"><div class="icon"></div><h3>VALUABLE</h3><p>Lorem ipsum dolor sit amonsectetur adipiscing incididunt ut labore et</p></div>
  </div>
  <div class="card" style="left:837px">
    <div class="bracket-frame" style="left:0;top:0;width:218px;height:217px"><div class="t-gold" style="width:150px;height:6px"></div><div class="l-gold" style="height:162px;width:6px"></div><div class="t-grey" style="width:60px;height:6px"></div><div class="r-grey" style="height:65px;width:6px"></div><div class="r-gold" style="height:145px;width:6px"></div><div class="b-gold" style="width:75px;height:7px"></div></div>
    <div class="body"><div class="icon"></div><h3>DEDICATED</h3><p>Lorem ipsum dolor sit amonsectetur adipiscing incididunt ut labore et</p></div>
  </div>
</section>

<section class="contact">
  <h2 class="section-title" style="top:1935px">CONTACT US</h2>
  <div class="field" style="left:233px;top:2038px;width:361px;height:54px">First Name</div>
  <div class="field" style="left:604px;top:2038px;width:362px;height:54px">Last Name</div>
  <div class="field" style="left:233px;top:2103px;width:361px;height:54px">Email address</div>
  <div class="field" style="left:604px;top:2103px;width:362px;height:54px">Phone Number</div>
  <div class="field" style="left:233px;top:2168px;width:733px;height:116px">Message</div>
  <div class="btn" style="left:507px;top:2314px;width:187px;height:38px">SUBMIT MESSAGE</div>
</section>

<footer>
  <div class="abs foot-gold"></div>
  <div class="abs foot-dark"></div>
  <div class="abs foot-dark-right"></div>
  <div class="abs foot-name"><div class="mark"></div><span>KEYSTONE<br>RIDGE<br>ADVISORS</span></div>
  <div class="social" style="left:553px" aria-label="Social link"></div>
  <div class="social" style="left:625px" aria-label="Social link"></div>
  <div class="social" style="left:696px" aria-label="Social link"></div>
  <div class="social" style="left:768px" aria-label="Social link"></div>
  <div class="abs ql-title">QUICK LINKS</div>
  <div class="abs ql"><span>Home</span><span>About us</span><span>Services</span><span>Contact us</span></div>
  <div class="abs news-title">SIGN UP NEWSLETTER</div>
  <div class="abs news-input">Enter Email</div>
  <div class="abs news-btn">SIGN UP</div>
  <p class="abs copy">© 2021 Keystone Ridge Advisors. All rights reserved &nbsp;|&nbsp; Privacy &nbsp;|&nbsp; Terms of Use</p>
</footer>
</body>
</html>
```